Luminously Grounded Vitality

We want to design a business card that is modern and appealing for an innovative psychedelic telemedicine company that provides at-home ketamine-assisted therapy along with wellness, longevity, and anti-aging medicines. We want to use our deep purple and white plus other colors you can find on our website. We don't have any strict brand guidelines yet so feel free to get creative. We want a very professional, but technology first modern design that will instill trust, peace, calm, but also be attractive to investors in the healthcare and SaaS space.

```html
<!DOCTYPE html>
<html lang="en">
<head>
<meta charset="utf-8">
<title>Luminously Grounded Vitality — Business Card</title>
<link href="https://fonts.googleapis.com/css2?family=Lato:wght@300;400;700&display=swap" rel="stylesheet">
<style>
  :root {
    --backdrop: #7d68a6;
    --brand-purple: #7c63a8;
    --card-white: #ffffff;
    --ink: #2a2a2a;
  }
  html, body {
    margin: 0;
    padding: 0;
    width: 1200px;
    height: 1136px;
    overflow: hidden;
    background: var(--backdrop);
    font-family: "Lato", sans-serif;
  }
  .canvas { position: relative; width: 1200px; height: 1136px; }
  .card {
    position: absolute;
    top: 217px;
    width: 401px;
    height: 700px;
    border-radius: 26px;
    overflow: hidden;
  }
  .card-front { left: 135px; background: var(--card-white); }
  .card-back { left: 665px; background: var(--brand-purple); }

  .front-mark {
    position: absolute;
    top: 60px; left: 0; width: 100%;
    text-align: center;
  }
  .front-mark .mark-dot {
    width: 110px; height: 110px; border-radius: 50%;
    background: var(--brand-purple);
    margin: 0 auto 26px;
  }
  .front-mark .mark-name {
    font-weight: 700;
    font-size: 26px;
    line-height: 1.2;
    color: var(--brand-purple);
  }

  .person-name {
    position: absolute; left: 37px; top: 383px;
    margin: 0; font-size: 28px; font-weight: 700;
    color: var(--brand-purple); letter-spacing: -0.2px;
  }
  .person-title {
    position: absolute; left: 37px; top: 420px;
    margin: 0; font-size: 16px; color: var(--ink);
  }
  .address-block {
    position: absolute; left: 58px; right: 0; top: 454px;
    height: 56px;
    border-top: 1.5px solid var(--brand-purple);
    border-bottom: 1.5px solid var(--brand-purple);
  }
  .address-block p {
    margin: 7px 0 0; font-size: 16.5px; line-height: 20px; color: var(--ink);
  }
  .address-block .icon { position: absolute; left: -22px; top: 19px; }

  .contact-list {
    position: absolute; left: 37px; top: 536px;
    margin: 0; padding: 0; list-style: none;
  }
  .contact-list li {
    display: flex; align-items: center;
    height: 23.5px; font-size: 16.5px; color: var(--ink);
  }
  .contact-list .icon { width: 14px; height: 14px; margin-right: 7px; flex: none; }
  .contact-list .social-square {
    width: 12px; height: 12px; background: var(--brand-purple);
    border-radius: 2px; margin: 0 9px 0 1px;
  }

  .back-mark {
    position: absolute; left: 0; top: 248px; width: 100%;
    text-align: center;
  }
  .back-mark .mark-dot {
    width: 84px; height: 84px; border-radius: 50%;
    background: var(--card-white); margin: 0 auto 30px;
  }
  .back-mark .mark-name {
    font-weight: 400; font-size: 34px; line-height: 1.15;
    color: var(--card-white); letter-spacing: -0.3px;
  }
</style>
</head>
<body>
<main class="canvas">
  <section class="card card-front">
    <div class="front-mark">
      <div class="mark-dot"></div>
      <div class="mark-name">Luminously<br>Grounded Vitality</div>
    </div>

    <h1 class="person-name">Daniel Reyes</h1>
    <p class="person-title">Ceo &amp; Founder</p>

    <div class="address-block">
      <svg class="icon" width="14" height="18" viewBox="0 0 14 18" aria-hidden="true">
        <path d="M7 0C3.1 0 0 3 0 6.8 0 11.5 7 18 7 18s7-6.5 7-11.2C14 3 10.9 0 7 0zm0 9.5a2.7 2.7 0 1 1 0-5.4 2.7 2.7 0 0 1 0 5.4z" fill="var(--brand-purple)"/>
      </svg>
      <p>482 Alder Avenue, Suite 210<br>Boulder, CO, United States, 80301</p>
    </div>

    <ul class="contact-list">
      <li>
        <svg class="icon" viewBox="0 0 14 14" aria-hidden="true"><rect x="3" y="0.5" width="8" height="13" rx="1.5" fill="none" stroke="var(--brand-purple)" stroke-width="1.4"/><circle cx="7" cy="11" r="0.9" fill="var(--brand-purple)"/></svg>
        (555) 318-2047
      </li>
      <li>
        <svg class="icon" viewBox="0 0 14 14" aria-hidden="true"><path d="M3 1l2.2 2.6-1.2 1.6c.8 1.8 2.2 3.2 4 4l1.6-1.2L12.2 10.2 11 12.6C6 12 2 8 1.4 3z" fill="var(--brand-purple)"/></svg>
        (555) 318-2047
      </li>
      <li>
        <svg class="icon" viewBox="0 0 14 14" aria-hidden="true"><rect x="0.5" y="2.5" width="13" height="9.5" fill="var(--brand-purple)"/><path d="M0.5 2.5L7 7.5l6.5-5" fill="none" stroke="#fff" stroke-width="1.2"/></svg>
        hello@luminouslyvitality.com
      </li>
      <li>
        <svg class="icon" viewBox="0 0 14 14" aria-hidden="true"><circle cx="7" cy="7" r="6.2" fill="none" stroke="var(--brand-purple)" stroke-width="1.3"/><path d="M1 7h12M7 1c2 2 2 10 0 12M7 1c-2 2-2 10 0 12" fill="none" stroke="var(--brand-purple)" stroke-width="1"/></svg>
        www.luminouslyvitality.com
      </li>
      <li>
        <span class="social-square"></span>
        @luminouslyvitality
      </li>
    </ul>
  </section>

  <section class="card card-back">
    <div class="back-mark">
      <div class="mark-dot"></div>
      <div class="mark-name">Luminously<br>Grounded Vitality</div>
    </div>
  </section>
</main>
</body>
</html>
```